packaging design for disposable trash bag

We need 3 design for 3 of our products. first item is trash bag,the second item is disposable table cover and third is food packaging bag . We are a company in Singapore selling disposable product. This packaging products will be sold on shelf or online.

Attached is the requirement of the product. And some samples.

Target Market(s)

adult, most likely housewife

Requirements
Must have
• Packing design requirement for trash bag
• 1. Include company logo design, which is attached in the creative brief. VARNEY TULK PLASTIC.
• 2. Clear showing of the product and its illustration of using. Eg. The trash bin.
• 3. Allocate a box for the purpose of sticking product size sticker.
• 4. Each packing bag holds 10pcs
• 5. Show of country of origin. Product of Singapore.
• 6. Use of one colour for printing of packing bag ( Black / blue/ bright Green/ white )
• 7. Show of warning: Keep polythene bags away from young children
• 8. dimension of the packagaing printing area : Lenght : 20 cm , Height 26 cm
• Packing design requirement for disposable Table Cover
• 1. Include company logo design, which is attached in the creative brief. Our company is VARNEY TULK PLASTIC.
• 2. Clear showing of the product and its illustration of using. Eg. The table?.
• 4. Each packing bag holds 5pcs
• 6. Use of one colour for printing of the packing bag ( Black / blue/ bright Green )
• Packing design requirement for disposable food packaging plastic bag
• 2. Clear showing of the product and its illustration of using. Eg. Food?.
• 4. Show of country of origin. Product of Singapore.
• 5. Use of one colour for printing of the packing bag ( Black/ bright green )
• 6. Show of warning: Keep polythene bags away from young children
• 7. Show of product information: hygienic, food grade, freezer resistance, grease proof, damp proof, heat resistant.
• 8. Include the open here packing opening.
• 9. dimension of the packagaing printing area : Lenght : 15 cm , Height 22 cm
Nice to have
• requirement is stated in the must have. Good to allocate some space beside the packaging PCS area for promotion stickers . And also space allocated for bar code stickers.
Should not have
• no more than one color for printing

```html
<!DOCTYPE html>
<html lang="en">
<head>
<meta charset="utf-8">
<title>Garbage Bag Packaging</title>
<link rel="stylesheet" href="https://fonts.googleapis.com/css2?family=League+Gothic&family=Arimo:wght@400;700&display=swap">
<style>
  :root {
    --ink: #229a4a;
    --bag: #c6cad7;
    --bag-light: #d3d6e0;
  }
  * { margin: 0; padding: 0; box-sizing: border-box; }
  html, body { width: 918px; height: 1200px; overflow: hidden; background: var(--bag); }
  .pack {
    position: absolute; left: 30px; top: 40px;
    width: 858px; height: 1118px;
    border: 3px solid var(--ink); border-radius: 10px;
    background: radial-gradient(ellipse at 50% 45%, var(--bag-light), var(--bag) 70%);
    color: var(--ink);
    font-family: "Arimo", Arial, sans-serif;
    overflow: hidden;
  }
  .pack > * { position: absolute; }
  .band, .rule { background: var(--ink); }

  .headline {
    font-family: "League Gothic", "Arial Narrow", sans-serif;
    font-size: 195px; line-height: 1; white-space: nowrap;
    transform: scaleX(0.8); transform-origin: left top;
  }
  .headline-1 { left: 31px; top: -1px; }
  .headline-2 { left: 31px; top: 158px; }

  .qty-label { left: 475px; top: 53px; font-weight: 700; font-size: 17px; line-height: 19px; letter-spacing: 0.5px; }
  .qty-value {
    left: 608px; top: 45px; font-family: "League Gothic", sans-serif;
    font-size: 84px; line-height: 1; white-space: nowrap;
  }
  .size-tag {
    left: 622px; top: 131px; width: 74px; text-align: center; background: var(--bag-light);
    font-weight: 700; font-size: 25px; line-height: 26px; letter-spacing: 1px;
  }
  .sticker-label { font-weight: 700; text-align: center; }
  .size-label { left: 459px; width: 393px; top: 228px; font-size: 23px; }

  .bins-art { left: 19px; top: 453px; width: 400px; height: 249px; background: linear-gradient(180deg, #2aa354, var(--ink)); border-radius: 10px; opacity: 0.85; }
  .bins-caption { left: 0; width: 444px; top: 720px; text-align: center; font-weight: 700; font-size: 17px; letter-spacing: 1px; }

  .eco-title {
    left: 546px; top: 411px; font-family: "League Gothic", sans-serif;
    font-size: 64px; line-height: 1; white-space: nowrap;
    transform: scaleX(0.62); transform-origin: left top;
  }
  .eco-badge { left: 569px; top: 477px; width: 180px; height: 130px; border-radius: 50%; background: radial-gradient(circle, #3bb065, var(--ink)); opacity: 0.8; }
  .care-note { left: 459px; width: 393px; top: 678px; text-align: center; font-weight: 700; font-size: 15px; line-height: 20.5px; }
  .disposal-icons { left: 580px; top: 757px; width: 160px; height: 68px; }

  .brand-mark { left: 196px; top: 877px; width: 50px; height: 52px; background: var(--ink); }
  .brand-name { left: 0; width: 461px; top: 944px; text-align: center; font-size: 23px; line-height: 24px; }
  .brand-web { left: 0; width: 461px; top: 998px; text-align: center; font-weight: 700; font-size: 18px; }

  .origin { left: 461px; width: 391px; top: 870px; text-align: center; font-size: 19px; }
  .barcode-label { left: 461px; width: 391px; top: 953px; font-size: 20px; }

  .warning { left: 16px; top: 1068px; font-weight: 700; font-size: 20px; white-space: nowrap; line-height: 30px; }
  .warning strong { font-size: 26px; letter-spacing: 1px; margin-right: 6px; }
</style>
</head>
<body>
<div class="pack">
  <!-- title block -->
  <div class="headline headline-1">GARBAGE</div>
  <div class="headline headline-2">BAG</div>
  <div class="rule" style="left:458px;top:0;width:3px;height:340px;"></div>

  <!-- quantity & size sticker -->
  <div class="band" style="left:459px;top:19px;width:393px;height:20px;"></div>
  <div class="qty-label">CONTENT<br>QUANTITY</div>
  <div class="qty-value">10 PIECES</div>
  <div class="band" style="left:459px;top:134px;width:393px;height:21px;"></div>
  <div class="size-tag">SIZE</div>
  <svg style="left:470px;top:164px;" width="378" height="160" viewBox="0 0 378 160" fill="none" stroke="#229a4a" stroke-width="3">
    <path d="M2 36V2H36M342 2H376V36M376 124V158H342M36 158H2V124"/>
  </svg>
  <div class="sticker-label size-label">SIZE (DIMENSION)</div>

  <div class="band" style="left:0;top:337px;width:852px;height:22px;"></div>

  <!-- product use -->
  <div class="bins-art" role="img" aria-label="Illustration of three waste bins: a lidded bin, a wheelie bin and a swing-top bin"></div>
  <div class="bins-caption">SUITABLE FOR ALL TYPES OF BINS</div>

  <div class="eco-title">OXO-BIODEGRADABLE</div>
  <div class="eco-badge" role="img" aria-label="Go green emblem with leaves and an upward arrow"></div>
  <div class="care-note">USED BAGS SHOULD BE TIED PROPERLY<br>BEFORE DISPOSAL TO ENSURE CLEANLINESS<br>TO THE SURROUNDING ENVIRONMENT.</div>
  <svg class="disposal-icons" viewBox="0 0 168 70" fill="none" stroke="#229a4a" stroke-width="3">
    <path d="M28 6L48 42H8Z" stroke-linejoin="round"/>
    <text x="28" y="36" fill="#229a4a" stroke="none" text-anchor="middle" font-family="Arimo, sans-serif" font-weight="700" font-size="16">2</text>
    <text x="28" y="62" fill="#229a4a" stroke="none" text-anchor="middle" font-family="Arimo, sans-serif" font-weight="700" font-size="11">HDPE</text>
    <circle cx="91" cy="26" r="22" fill="#229a4a" stroke="none"/>
    <path d="M80 30a12 12 0 1 0 6-14" stroke="#c6cad7" stroke-width="5"/>
    <path d="M80 10l7 6-8 4z" fill="#c6cad7" stroke="none"/>
    <circle cx="152" cy="8" r="4" fill="#229a4a" stroke="none"/>
    <path d="M152 14v22M146 20l6 4M152 36l-4 14M152 36l4 14"/>
    <path d="M126 28h14l-2 22h-10z" stroke-width="2.5"/>
  </svg>

  <!-- company & origin -->
  <div class="band" style="left:0;top:843px;width:461px;height:20px;"></div>
  <div class="rule" style="left:461px;top:843px;width:391px;height:3px;"></div>
  <div class="rule" style="left:459px;top:843px;width:3px;height:205px;"></div>
  <div class="brand-mark"></div>
  <div class="brand-name">VARNEY TULK PLASTIC<br>PTE LTD</div>
  <div class="brand-web">www.varneytulkplastic.com</div>

  <div class="origin">PRODUCT OF SINGAPORE</div>
  <svg style="left:541px;top:910px;" width="236" height="108" viewBox="0 0 236 108" fill="none" stroke="#229a4a" stroke-width="3">
    <path d="M2 28V2H28M208 2H234V28M234 80V106H208M28 106H2V80"/>
  </svg>
  <div class="sticker-label barcode-label">BARCODE</div>

  <div class="band" style="left:0;top:1029px;width:461px;height:19px;"></div>
  <div class="rule" style="left:461px;top:1045px;width:391px;height:3px;"></div>

  <!-- warning -->
  <div class="warning"><strong>WARNING:</strong>PLEASE KEEP POLYTHENE BAGS AWAY FROM YOUNG CHILDREN</div>
</div>
</body>
</html>
```